Design few pages for professional development app

I need a website design for a prototype project. The goal of the project is to prototype a few basic screens for a professional development application.

The final design should be clean, modern, and appeal to a professional millenial clientele.The designs have been wireframed (see attached), and we'd like these wireframes converted to design files.

Here is the list of goals and tasks that correspond to the design: https://sheets.plorvane.com/tables/d/7qWmK84x9PLzn3oTcB2vEaRyhUDs-kfNJ52tqXyMHw/edit?usp=sharing

Number of Pages Required

5+ page

Font styles to use
Serif
Sans Serif

Colors

Designer to choose colors to be used in the design.

Requirements
Nice to have
• Uses Google Material Design, Bootstrap, or another framework

```html
<!DOCTYPE html>
<html lang="en">
<head>
<meta charset="UTF-8">
<title>ClimbWell – Suggested Tasks</title>
<link href="https://fonts.googleapis.com/css2?family=Nunito:wght@400;600;700&display=swap" rel="stylesheet">
<style>
  :root {
    --page-bg: #ebf0f4;
    --white: #ffffff;
    --ink: #3d4a5c;
    --body-text: #4a5361;
    --muted: #7d8794;
    --brand: #1e73d2;
    --button: #1976d2;
    --button-soft: #c5dcf2;
    --search-bg: #d6dee6;
    --brand-bg: #fde0c5; --brand-fg: #f07c10;
    --promo-bg: #d9e8d2; --promo-fg: #5aa02c;
    --leader-bg: #fde8c4; --leader-fg: #f5a00e;
    --network-bg: #bfe4e6; --network-fg: #1a95a0;
  }
  * { box-sizing: border-box; margin: 0; padding: 0; }
  html, body { width: 1200px; height: 675px; overflow: hidden; }
  body { background: var(--page-bg); font-family: "Nunito", sans-serif; position: relative; }

  .topbar { position: absolute; left: 0; top: 0; width: 1200px; height: 50px; background: var(--white); }
  .wordmark { position: absolute; left: 24px; top: 14px; font-size: 15px; font-weight: 700; color: var(--brand); }
  .search-btn { position: absolute; left: 1022px; top: 10px; width: 30px; height: 30px; border-radius: 5px; background: var(--search-bg); display: flex; align-items: center; justify-content: center; }
  .avatar { position: absolute; left: 1071px; top: 10px; width: 30px; height: 30px; border-radius: 6px; background: linear-gradient(135deg, #3a2a22, #c99478); }
  .user-name { position: absolute; left: 1109px; top: 17px; font-size: 11px; font-weight: 600; color: var(--ink); }

  .page-title { position: absolute; left: 251px; top: 106px; font-size: 22.5px; font-weight: 700; color: var(--ink); }

  .task-card { position: absolute; width: 219px; height: 169px; background: var(--white); border-radius: 8px; overflow: hidden; }
  .task-head { height: 36px; display: flex; align-items: center; justify-content: space-between; padding: 0 18px; font-size: 14px; font-weight: 600; }
  .task-head svg { width: 20px; height: 20px; }
  .task-body { padding: 16px 19px 0; }
  .task-text { font-size: 10.6px; line-height: 17px; color: var(--body-text); height: 34px; }
  .task-meta { margin-top: 4px; display: flex; align-items: center; gap: 5px; font-size: 9.4px; font-weight: 600; color: var(--muted); height: 14px; }
  .task-meta svg { width: 12px; height: 12px; }
  .task-btn { margin-top: 13px; height: 31px; border-radius: 4px; background: var(--button); color: var(--white); font-size: 10.6px; font-weight: 700; display: flex; align-items: center; justify-content: center; }
  .task-btn.is-done { background: var(--button-soft); color: var(--button); font-weight: 600; }

  .theme-brand .task-head { background: var(--brand-bg); color: var(--brand-fg); }
  .theme-promo .task-head { background: var(--promo-bg); color: var(--promo-fg); }
  .theme-leader .task-head { background: var(--leader-bg); color: var(--leader-fg); }
  .theme-network .task-head { background: var(--network-bg); color: var(--network-fg); }

  .col-1 { left: 253px; } .col-2 { left: 491px; } .col-3 { left: 728px; }
  .row-1 { top: 166px; } .row-2 { top: 354px; }
</style>
</head>
<body>
  <header class="topbar">
    <div class="wordmark">ClimbWell</div>
    <div class="search-btn">
      <svg width="14" height="14" viewBox="0 0 24 24" fill="none" stroke="#7d8794" stroke-width="2.6" stroke-linecap="round"><circle cx="10" cy="10" r="6.5"/><line x1="15" y1="15" x2="21" y2="21"/></svg>
    </div>
    <div class="avatar" role="img" aria-label="Profile photo of the user"></div>
    <div class="user-name">Nora Ellis</div>
  </header>

  <h1 class="page-title">Nora, here’s your list of suggested tasks</h1>

  <!-- Row 1 -->
  <section class="task-card theme-brand col-1 row-1">
    <div class="task-head">Personal Branding
      <svg viewBox="0 0 24 24" fill="none" stroke="currentColor" stroke-width="2" stroke-linejoin="round"><circle cx="6" cy="4" r="2"/><circle cx="18" cy="4" r="2"/><circle cx="12" cy="9" r="5"/><path d="M5 22l2-7h10l2 7z"/></svg>
    </div>
    <div class="task-body">
      <p class="task-text">Write your personal brand statement.</p>
      <div class="task-meta">
        <svg viewBox="0 0 24 24" fill="none" stroke="#7d8794" stroke-width="2"><rect x="3" y="3" width="18" height="18"/><path d="M7 12l4 4 6-8"/></svg>
        Completed on Sep 15th, 19
      </div>
      <div class="task-btn is-done">Completed</div>
    </div>
  </section>

  <section class="task-card theme-promo col-2 row-1">
    <div class="task-head">Get a Promotion
      <svg viewBox="0 0 24 24" fill="none" stroke="currentColor" stroke-width="2" stroke-linejoin="round"><rect x="3" y="8" width="18" height="5"/><rect x="5" y="13" width="14" height="9"/><line x1="12" y1="8" x2="12" y2="22"/><path d="M12 8C10 3 6 3 7 6s5 2 5 2zM12 8c2-5 6-5 5-2s-5 2-5 2z"/></svg>
    </div>
    <div class="task-body">
      <p class="task-text">Have a career conversation with your manager.</p>
      <div class="task-meta">
        <svg viewBox="0 0 24 24" fill="none" stroke="#7d8794" stroke-width="2" stroke-linecap="round"><circle cx="12" cy="13" r="8"/><path d="M12 9v4l3 2M3 5l3-2M21 5l-3-2"/></svg>
        57% complete
      </div>
      <div class="task-btn">Start Task</div>
    </div>
  </section>

  <section class="task-card theme-promo col-3 row-1">
    <div class="task-head">Get a Promotion
      <svg viewBox="0 0 24 24" fill="none" stroke="currentColor" stroke-width="2" stroke-linejoin="round"><rect x="3" y="8" width="18" height="5"/><rect x="5" y="13" width="14" height="9"/><line x1="12" y1="8" x2="12" y2="22"/><path d="M12 8C10 3 6 3 7 6s5 2 5 2zM12 8c2-5 6-5 5-2s-5 2-5 2z"/></svg>
    </div>
    <div class="task-body">
      <p class="task-text">Ask 4 peers for candid feedback.</p>
      <div class="task-meta">
        <svg viewBox="0 0 24 24" fill="none" stroke="#7d8794" stroke-width="2" stroke-linecap="round"><circle cx="12" cy="13" r="8"/><path d="M12 9v4l3 2M3 5l3-2M21 5l-3-2"/></svg>
        30min to Complete
      </div>
      <div class="task-btn">Start Task</div>
    </div>
  </section>

  <!-- Row 2 -->
  <section class="task-card theme-leader col-1 row-2">
    <div class="task-head">Be a Better Leader
      <svg viewBox="0 0 24 24" fill="none" stroke="currentColor" stroke-width="2" stroke-linejoin="round"><path d="M3 9h5l11-6v16L8 13H3z"/><path d="M6 13l2 8h3l-1-8"/><path d="M21 8v4"/></svg>
    </div>
    <div class="task-body">
      <p class="task-text">Solicit feedback from your direct reports.</p>
      <div class="task-meta">
        <svg viewBox="0 0 24 24" fill="none" stroke="#7d8794" stroke-width="2" stroke-linecap="round"><circle cx="12" cy="13" r="8"/><path d="M12 9v4l3 2M3 5l3-2M21 5l-3-2"/></svg>
        60min to Complete
      </div>
      <div class="task-btn">Start Task</div>
    </div>
  </section>

  <section class="task-card theme-network col-2 row-2">
    <div class="task-head">Build my Network
      <svg viewBox="0 0 24 24" fill="none" stroke="currentColor" stroke-width="2" stroke-linejoin="round"><path d="M3 2l6 5h6l6-5"/><path d="M10 7h4l-1 3h-2z"/><path d="M11 10l-1.5 9L12 22l2.5-3L13 10"/></svg>
    </div>
    <div class="task-body">
      <p class="task-text">Invite someone in a different department for a “Get to Know…”</p>
      <div class="task-meta">
        <svg viewBox="0 0 24 24" fill="none" stroke="#7d8794" stroke-width="2" stroke-linecap="round"><circle cx="12" cy="12" r="9"/><path d="M12 7v5l3 2"/></svg>
        45min to Complete
      </div>
      <div class="task-btn">Start Task</div>
    </div>
  </section>

  <section class="task-card theme-leader col-3 row-2">
    <div class="task-head">Be a Better Leader
      <svg viewBox="0 0 24 24" fill="none" stroke="currentColor" stroke-width="2" stroke-linejoin="round"><path d="M3 9h5l11-6v16L8 13H3z"/><path d="M6 13l2 8h3l-1-8"/><path d="M21 8v4"/></svg>
    </div>
    <div class="task-body">
      <p class="task-text">Delegate something you currently do to your direct report.</p>
      <div class="task-meta">
        <svg viewBox="0 0 24 24" fill="none" stroke="#7d8794" stroke-width="2" stroke-linecap="round"><circle cx="12" cy="13" r="8"/><path d="M12 9v4l3 2M3 5l3-2M21 5l-3-2"/></svg>
        60min to Complete
      </div>
      <div class="task-btn">Start Task</div>
    </div>
  </section>
</body>
</html>
```